Mezzanine Floor Manufacturer looking for a new business card design

We manufacture mezzanine floors and are providers of racking systems. We provide a range of items/services - simple rack repairs , full warehouse fit outs , manufacturer and install mezzanine floors , partitioning and large turnkey projects. Recently had a new website - www.corvane-shelving.co.uk and would like our business cards updating aswell . Our current card is single sided in the old logo colours (pdf attached) and needs updating.

Target Market(s)

We deal with large projects/ multi national companies and also smaller projects and companies throughout the UK ranging from a single warehouse to a large multi site company.

Industry/Entity Type

Business

Contact Information for Business Card

Will have job title,tel no's, email ,website address etc like example pdf

Requirements
Must have
• Hi - needs to use the colours of the logo & new website. Card needs to be professional

```html
<!DOCTYPE html>
<html lang="en">
<head>
<meta charset="utf-8">
<title>Corvane Shelving – Business Card</title>
<link href="https://fonts.googleapis.com/css2?family=Oswald:wght@600&family=Rajdhani:wght@500;600;700&display=swap" rel="stylesheet">
<style>
  :root{
    --bg:#2a2a2c;
    --paper:#ffffff;
    --paper-shade:#f1f1f1;
    --red:#c0302a;
    --red-deep:#9c211c;
    --ink:#1d1d1f;
    --ink-soft:#555;
    --on-red:#f7eceb;
  }
  *{box-sizing:border-box;margin:0;padding:0}
  html,body{width:1200px;height:900px;overflow:hidden}
  body{
    background:var(--bg);
    font-family:"Rajdhani",sans-serif;
    display:flex;align-items:center;justify-content:center;gap:40px;
  }
  .card{
    width:560px;height:330px;position:relative;overflow:hidden;
    background:linear-gradient(180deg,var(--paper),var(--paper-shade));
    box-shadow:0 10px 30px rgba(0,0,0,.45);
  }
  .wordmark{
    display:flex;align-items:center;gap:10px;
    color:var(--red);font-family:"Rajdhani",sans-serif;font-weight:700;
    letter-spacing:2px;
  }
  .wordmark .dot{width:14px;height:14px;border-radius:50%;background:var(--red)}

  /* back */
  .card--back .wordmark{position:absolute;left:60px;top:118px;font-size:54px}
  .card--back .wordmark .dot{width:22px;height:22px}
  .address{
    position:absolute;left:150px;top:200px;
    color:var(--red);font-size:17px;font-weight:600;line-height:1.3;
  }

  /* front */
  .card--front .band{
    position:absolute;left:0;right:0;top:148px;bottom:0;
    background:linear-gradient(90deg,var(--red),var(--red-deep));
  }
  .card--front .wordmark{position:absolute;left:34px;top:54px;font-size:40px}
  .person{position:absolute;right:30px;top:28px;text-align:right}
  .person__name{font-family:"Oswald",sans-serif;font-weight:600;font-size:27px;color:var(--ink);letter-spacing:.5px;line-height:1}
  .person__role{font-size:16px;color:var(--ink-soft);font-weight:500;margin-top:2px}
  .contacts{position:absolute;left:30px;top:172px;list-style:none}
  .contacts li{display:flex;align-items:center;gap:16px;color:var(--on-red);font-size:17px;font-weight:500;height:28px;letter-spacing:.3px}
  .contacts svg{width:16px;height:16px;fill:none;stroke:var(--on-red);stroke-width:1.8}
  .services{position:absolute;left:370px;top:152px;list-style:none}
  .services li{color:var(--on-red);font-size:14.5px;font-weight:600;letter-spacing:.6px;line-height:19px;text-transform:uppercase}
  .services li::before{content:"• "}
</style>
</head>
<body>

<section class="card card--back">
  <div class="wordmark"><span class="dot"></span>CORVANE</div>
  <p class="address">Unit 4, Larkfield Business Park<br>Ashbrook, Hollingshire DX9 4QT</p>
</section>

<section class="card card--front">
  <div class="band"></div>
  <div class="wordmark"><span class="dot"></span>CORVANE</div>
  <div class="person">
    <p class="person__name">MARTIN HALE</p>
    <p class="person__role">technical sales</p>
  </div>
  <ul class="contacts">
    <li><svg viewBox="0 0 16 16"><path d="M4 2l2 3-1.5 1.5a8 8 0 0 0 5 5L11 10l3 2-1.5 2.5C7 14 2 9 1.5 3.5z"/></svg>01632 960481</li>
    <li><svg viewBox="0 0 16 16"><rect x="4.5" y="1.5" width="7" height="13" rx="1"/><path d="M7 12.5h2"/></svg>07700 900312</li>
    <li><svg viewBox="0 0 16 16"><rect x="4" y="1.5" width="8" height="4"/><rect x="1.5" y="5.5" width="13" height="6" rx="1"/><rect x="4" y="9.5" width="8" height="5"/></svg>01632 960529</li>
    <li><svg viewBox="0 0 16 16"><rect x="1.5" y="3.5" width="13" height="9"/><path d="M1.5 3.5L8 9l6.5-5.5"/></svg>martin@corvane-shelving.co.uk</li>
    <li><svg viewBox="0 0 16 16"><circle cx="8" cy="8" r="6.5"/><path d="M1.5 8h13M8 1.5c-3 3.5-3 9.5 0 13M8 1.5c3 3.5 3 9.5 0 13"/></svg>www.corvane-shelving.co.uk</li>
  </ul>
  <ul class="services">
    <li>Mezzanine Floors</li>
    <li>Cantilever Racking</li>
    <li>Pallet Racking</li>
    <li>Safety Barriers</li>
    <li>Longspan Shelving</li>
    <li>Steel Shelving</li>
    <li>Partitioning</li>
    <li>Turnkey Projects</li>
  </ul>
</section>

</body>
</html>
```